A Speech Therapy Business needs to update their logo

I need an update to the font and color of my logo to look more appealing. I am looking to open a private practice as a Speech Language Pathologist that caters to adults and children. It needs to be sophisticated and friendly at the same time. I want to keep the silhouette in my logo as is, just update the font and color for "Brightpaths".
Industry/Entity Type
Business
Contact Information for Business Card
I want the business card to have my logo, my name (Dorota Valk, CCC-SLP, TSSLD) and that I am a Bilingual Speech Language Pathologist. Also, include my phone number, (555) 271-8390. Include my website, Brightpathsslp.example, and email address, dorotavalk@brightpathsslp.example
Look and feel
Each slider illustrates characteristics of the customer's brand and the style your logo design should communicate.

```html
<!DOCTYPE html>
<html lang="en">
<head>
<meta charset="utf-8">
<title>Brightpaths Speech Therapy – Business Card</title>
<link href="https://fonts.googleapis.com/css2?family=Roboto:wght@400;500;700&family=Montserrat:wght@700;800&display=swap" rel="stylesheet">
<style>
  :root {
    --backdrop: #2b2b2b;
    --card-purple: #7a4fa6;
    --card-black: #0b0b0b;
    --bubble-white: #ffffff;
    --brand-purple: #6f46a0;
    --text-light: #f3eefa;
    --text-soft: #e4dbef;
    --silhouette: #1a1a1a;
  }
  * { margin: 0; padding: 0; box-sizing: border-box; }
  html, body {
    width: 1200px; height: 873px; overflow: hidden;
    background: var(--backdrop);
  }
  .canvas { position: relative; width: 1200px; height: 873px; }
  .card {
    position: absolute; left: 110px; top: 156px;
    width: 980px; height: 560px;
    border-radius: 28px; overflow: hidden;
    background: var(--card-purple);
    font-family: "Roboto", Arial, sans-serif;
  }
  .card-band { position: absolute; inset: 0; width: 100%; height: 100%; }
  .logo-bubble {
    position: absolute; left: 30px; top: 70px;
    width: 480px; height: 350px;
  }
  .logo-mark {
    position: absolute; left: 80px; top: 110px;
    width: 390px; height: 130px;
    border-radius: 10px;
    background: linear-gradient(90deg, var(--silhouette), #3a3a3a);
  }
  .logo-name {
    position: absolute; left: 78px; top: 252px;
    font-family: "Montserrat", Arial, sans-serif;
    font-weight: 800; font-size: 62px; line-height: 1;
    color: var(--brand-purple);
    letter-spacing: -0.5px;
  }
  .owner {
    position: absolute; left: 600px; top: 372px;
    color: var(--text-light);
  }
  .owner-name { font-size: 24px; font-weight: 700; letter-spacing: 0.3px; }
  .owner-name .credentials { font-weight: 400; }
  .owner-title {
    margin-top: 6px;
    font-size: 14px; letter-spacing: 0.8px; color: var(--text-soft);
  }
  .contacts {
    position: absolute; right: 410px; top: 432px;
    list-style: none; text-align: right;
    color: var(--text-light); font-size: 22px; line-height: 32px;
  }
  .contacts li { display: flex; justify-content: flex-end; align-items: center; gap: 12px; }
  .contact-icon { width: 18px; height: 18px; flex: none; }
</style>
</head>
<body>
<main class="canvas">
  <article class="card">
    <svg class="card-band" viewBox="0 0 980 560" aria-hidden="true">
      <polygon points="0,0 980,0 980,150 0,290" fill="var(--card-black)"/>
    </svg>

    <svg class="logo-bubble" viewBox="0 0 480 350" aria-hidden="true">
      <path d="M55 0 H425 Q480 0 480 55 V245 Q480 300 425 300 L470 348 L360 300 H55 Q0 300 0 245 V55 Q0 0 55 0 Z" fill="var(--bubble-white)"/>
    </svg>
    <div class="logo-mark" role="img" aria-label="Silhouette row of people holding hands, from adults to a small child, with a small heart"></div>
    <div class="logo-name">Brightpaths</div>

    <div class="owner">
      <p class="owner-name">DOROTA VALK, <span class="credentials">CCC-SLP, TSSLD</span></p>
      <p class="owner-title">BILINGUAL SPEECH LANGUAGE PATHOLOGIST</p>
    </div>

    <ul class="contacts">
      <li>(555) 271-8390
        <svg class="contact-icon" viewBox="0 0 16 16" aria-hidden="true"><rect width="16" height="16" rx="3" fill="var(--text-light)"/><path d="M5 3.5l1.6 2.4-1 1c.6 1.3 1.5 2.2 2.8 2.8l1-1L12 10.3 11 12.4C7.5 12.2 3.8 8.5 3.6 5z" fill="var(--card-purple)"/></svg>
      </li>
      <li>dorotavalk@brightpathsslp.example
        <svg class="contact-icon" viewBox="0 0 16 16" aria-hidden="true"><rect width="16" height="16" rx="3" fill="var(--text-light)"/><rect x="3" y="4.5" width="10" height="7" fill="none" stroke="var(--card-purple)" stroke-width="1.4"/><path d="M3 4.5l5 4 5-4" fill="none" stroke="var(--card-purple)" stroke-width="1.4"/></svg>
      </li>
      <li>www.brightpathsslp.example
        <svg class="contact-icon" viewBox="0 0 16 16" aria-hidden="true"><rect width="16" height="16" rx="3" fill="var(--text-light)"/><circle cx="8" cy="8" r="4.8" fill="none" stroke="var(--card-purple)" stroke-width="1.2"/><ellipse cx="8" cy="8" rx="2" ry="4.8" fill="none" stroke="var(--card-purple)" stroke-width="1"/><path d="M3.2 8h9.6" stroke="var(--card-purple)" stroke-width="1"/></svg>
      </li>
    </ul>
  </article>
</main>
</body>
</html>
```